Copper Wren Coffee Roaster Locations and Cold Brew Billboard

We are a locally owned coffee roaster in Portland Oregon with three coffee shop locations on the east side of town.

Husband and wife started the company in 2007. We are in need of a billboard design by July 9, 2023.

We would like the billboard to focus on marketing our new produce line of Cold Brew Cans. And to advertise our three locations along with our wholesale service.

Here are some texts that we would like to include if it will fit.

Copper Wren Coffee Roaster
Portland’s Eastside roaster
Still Local and Family Owned
Single Origin Coffee , No Boring Blends
House made Vegan and Gluten Free pastries
Ask about Wholesale

Locations with their cross streets
Kellam location [ Kellam and 47th]
Lantern location [Marlo and 19th]
Brickell location [Brickell and 52nd Pl]

Pictures of our two cold brew cans
Logo: We have circular logo and text version. We are open to using both or just one depending on the layout of the design.

Included are the images and logos. And Spec Sheet for billboard.

```html
<!DOCTYPE html>
<html lang="en">
<head>
<meta charset="utf-8">
<title>Copper Wren Coffee Roaster Billboard</title>
<link rel="stylesheet" href="https://fonts.googleapis.com/css2?family=Roboto:wght@500;700;900&display=swap">
<style>
  :root {
    --page: #9a9a9a;
    --paper: #f4f4f4;
    --paper-shade: #e2e2e2;
    --ink: #111111;
    --purple: #5a1f78;
    --violet: #7b45c4;
    --gold: #f6c54a;
    --orange: #f8b42d;
    --cream: #f6efbe;
    --pin: #f3c23a;
  }
  * { box-sizing: border-box; margin: 0; padding: 0; }
  html, body { width: 1040px; height: 1200px; overflow: hidden; background: var(--page); }
  body { position: relative; font-family: "Roboto", Arial, sans-serif; color: var(--ink); }

  .billboard {
    position: absolute; left: 20px; top: 454px; width: 1000px; height: 292px;
    overflow: hidden;
    background: linear-gradient(120deg, var(--paper) 0%, #ffffff 35%, var(--paper-shade) 60%, var(--paper) 100%);
    box-shadow: 0 8px 18px rgba(0,0,0,0.35);
  }
  .billboard-shapes { position: absolute; inset: 0; }

  .brand-mark {
    position: absolute; left: 33px; top: 14px; width: 96px; height: 96px;
    border: 2px solid #3a3a3a; border-radius: 50%;
    display: flex; align-items: center; justify-content: center; text-align: center;
    font-weight: 700; font-size: 15px; line-height: 1.1; color: #3a3a3a;
  }

  .headline {
    position: absolute; left: 157px; top: 20px;
    font-weight: 900; font-size: 41px; line-height: 44px; letter-spacing: -0.3px;
  }
  .headline-rule {
    position: absolute; left: 157px; top: 114px; width: 264px; height: 2px; background: var(--purple);
  }

  .features { position: absolute; list-style: none; }
  .features li {
    position: relative; padding-left: 16px; height: 24px;
    font-weight: 500; font-size: 12px; line-height: 14px;
  }
  .features li::before {
    content: ""; position: absolute; left: 0; top: 1px; width: 11px; height: 11px;
    border-radius: 50%; border: 2.5px solid var(--gold);
  }
  .features li.purple::before { border-color: var(--purple); }
  .features-left { left: 52px; top: 142px; }
  .features-right { left: 253px; top: 141px; }

  .location {
    position: absolute; top: 224px; width: 150px; margin-left: -75px; text-align: center;
    font-weight: 500; font-size: 11.5px; line-height: 14px;
  }
  .location svg { display: block; margin: 0 auto 5px; }

  .can {
    position: absolute; border-radius: 18px / 12px;
    box-shadow: 6px 8px 12px rgba(0,0,0,0.3);
  }
  .can-dark {
    left: 582px; top: 20px; width: 150px; height: 258px; transform: rotate(4deg);
    background: linear-gradient(90deg, #ff6a2a 0%, #7a2aa8 12%, #1a1024 35%, #211232 80%, #6b3d9e 100%);
  }
  .can-light {
    left: 748px; top: 16px; width: 150px; height: 254px; transform: rotate(6deg);
    background: linear-gradient(90deg, #f39a1d 0%, #a6cf3a 12%, #fff8cf 40%, #f7f0b8 80%, #f3c43c 100%);
  }
</style>
</head>
<body>
  <section class="billboard">
    <svg class="billboard-shapes" viewBox="0 0 1000 292" width="1000" height="292" aria-hidden="true">
      <polygon points="420,0 1000,0 1000,292 560,292" fill="var(--violet)"/>
      <polygon points="640,0 930,0 1000,55 1000,150 770,292 560,292 560,170" fill="var(--orange)"/>
      <path d="M930,0 L1000,0 L1000,40 C980,30 955,30 945,18 C938,10 935,5 930,0 Z" fill="#ffffff"/>
      <polygon points="30,232 590,232 565,292 30,292" fill="var(--cream)"/>
      <path d="M0,210 C20,206 30,226 22,244 C14,262 40,270 70,292 L0,292 Z" fill="var(--purple)"/>
    </svg>

    <div class="brand-mark">Copper<br>Wren</div>

    <h1 class="headline">Copper Wren<br>Coffee Roaster</h1>
    <div class="headline-rule"></div>

    <ul class="features features-left">
      <li>Portland's Eastside roaster</li>
      <li class="purple">Single Origin Coffee</li>
      <li>Ask about Wholesale</li>
    </ul>
    <ul class="features features-right">
      <li class="purple">Still Local and Family Owned</li>
      <li>No Boring Blends</li>
      <li class="purple">House made Vegan and Gluten Free pastries</li>
    </ul>

    <div class="location" style="left:128px">
      <svg width="20" height="20" viewBox="0 0 20 20"><circle cx="10" cy="10" r="9" fill="var(--pin)" stroke="var(--purple)" stroke-width="1.5"/><path d="M10 4.5a3.5 3.5 0 0 0-3.5 3.5c0 2.6 3.5 6.5 3.5 6.5s3.5-3.9 3.5-6.5A3.5 3.5 0 0 0 10 4.5z" fill="var(--purple)"/><circle cx="10" cy="8" r="1.3" fill="var(--pin)"/></svg>
      Kellam location<br>[ Kellam and 47th]
    </div>
    <div class="location" style="left:277px">
      <svg width="20" height="20" viewBox="0 0 20 20"><circle cx="10" cy="10" r="9" fill="var(--pin)" stroke="var(--purple)" stroke-width="1.5"/><path d="M10 4.5a3.5 3.5 0 0 0-3.5 3.5c0 2.6 3.5 6.5 3.5 6.5s3.5-3.9 3.5-6.5A3.5 3.5 0 0 0 10 4.5z" fill="var(--purple)"/><circle cx="10" cy="8" r="1.3" fill="var(--pin)"/></svg>
      Lantern location<br>[Marlo and 19th]
    </div>
    <div class="location" style="left:432px">
      <svg width="20" height="20" viewBox="0 0 20 20"><circle cx="10" cy="10" r="9" fill="var(--pin)" stroke="var(--purple)" stroke-width="1.5"/><path d="M10 4.5a3.5 3.5 0 0 0-3.5 3.5c0 2.6 3.5 6.5 3.5 6.5s3.5-3.9 3.5-6.5A3.5 3.5 0 0 0 10 4.5z" fill="var(--purple)"/><circle cx="10" cy="8" r="1.3" fill="var(--pin)"/></svg>
      Brickell location<br>[Brickell and 52nd Pl]
    </div>

    <div class="can can-dark" role="img" aria-label="Product photo: dark roast cold brew can in black and purple"></div>
    <div class="can can-light" role="img" aria-label="Product photo: light roast cold brew can in cream, yellow and green"></div>
  </section>
</body>
</html>
```